Plakat-Design zum Thema Personalabteilung
sehr zufrieden, Änderungen wurden schnell umgesetzt und Kommunikation war sehr gut
Zielgruppe
Morvena Software hat sich zum Ziel gesetzt, kleinen und mittleren Unternehmen über das Web schnell einsetzbare Lösungen zur Verfügung zu stellen, die ohne große Projektkosten direkt von der Personalabteilung genutzt werden können.
Frauen mittleren Alters in der Personalabteilung.
Aufgabenstellung
Formatvorgaben siehe Dokument 'Druckdatenblatt_Grossplakat'.
Wie haben uns 2 Designvorschläge überlegt. Bitte wählen Sie mindestens einen Vorschlag oder machen Sie zu jedem Design einen Entwurf.
Vorschlag 1:
Variante 1:
Dicker ekliger Chef
Sprechblase 1: meine Tussi in der Personalabteilung arbeitet 24/7 für mich
Sprechblase 2: und das völlig kostenfrei
stabwerkel.net
Footer mit: Nordhafen – Weidenstadt – Kalmbrück/Eschau – Lindgau
Variante 2:
Headline: Neues aus der Personalabteilung
Sprechblase 1: meine Tussi arbeitet 24/7 für mich
Vorschlag 2:
Tussi (Avatar)
Sprechblase: Ich arbeite 24/7 für meinen Chef, völlig kostenfrei und ich liebe es
kanzleigrund.cloud

```html
<!DOCTYPE html>
<html lang="de">
<head>
<meta charset="utf-8">
<title>Neues aus der Personalabteilung – Plakat</title>
<link rel="stylesheet" href="https://fonts.googleapis.com/css2?family=Bangers&family=Patrick+Hand&display=swap">
<style>
  :root {
    --page: #f2f2f2;
    --yellow: #fdec00;
    --ink: #111111;
    --board-dark: #2a2e2f;
    --board-mid: #4a4f50;
    --pink: #e8368f;
    --green: #4fb537;
    --white: #ffffff;
  }
  * { margin: 0; padding: 0; box-sizing: border-box; }
  html, body { width: 1200px; height: 982px; overflow: hidden; background: var(--page); }
  .poster {
    position: absolute; left: 40px; top: 102px;
    width: 1120px; height: 778px; overflow: hidden;
    background: var(--board-dark);
  }
  .headline-band {
    position: absolute; left: 0; top: 0; width: 100%; height: 94px;
    background: var(--yellow);
    display: flex; align-items: center; justify-content: center;
  }
  .headline {
    font-family: "Bangers", system-ui, sans-serif;
    font-size: 68px; letter-spacing: 2.5px; color: var(--ink);
    font-weight: 400; padding-top: 14px; white-space: nowrap;
  }
  .photo {
    position: absolute; left: 0; top: 94px; width: 100%; height: 684px;
    background:
      radial-gradient(ellipse 28% 45% at 56% 55%, #c9b3a6 0%, #8f7466 45%, rgba(74,79,80,0) 75%),
      radial-gradient(ellipse 30% 25% at 58% 95%, #ece9e6 0%, rgba(236,233,230,0) 80%),
      radial-gradient(ellipse 80% 80% at 50% 50%, var(--board-mid) 0%, var(--board-dark) 100%);
  }
  .bubble { position: absolute; }
  .bubble-pink { left: 54px; top: 108px; width: 345px; height: 225px; }
  .bubble-green { left: 718px; top: 166px; width: 240px; height: 140px; }
  .bubble text {
    font-family: "Patrick Hand", cursive;
    fill: var(--white);
  }
  .locations {
    position: absolute; left: 870px; top: 612px; width: 220px;
    font-family: "Patrick Hand", cursive; font-size: 17px; line-height: 23px;
    color: var(--white); text-align: center; white-space: nowrap;
  }
  .url-band {
    position: absolute; left: 696px; top: 661px; width: 424px; height: 62px;
    background: var(--yellow);
    display: flex; align-items: center; padding-left: 14px;
  }
  .url {
    font-family: "Bangers", system-ui, sans-serif;
    font-size: 44px; letter-spacing: 3px; color: var(--ink); padding-top: 6px;
    white-space: nowrap;
  }
</style>
</head>
<body>
  <main class="poster">
    <header class="headline-band">
      <h1 class="headline">Neues aus der Personalabteilung</h1>
    </header>

    <div class="photo" role="img" aria-label="Foto: Frau mit Hochsteckfrisur, großer Brille, weißer Rüschenbluse und schwarzer Krawatte vor dunkler Kreidetafel"></div>

    <svg class="bubble bubble-pink" viewBox="0 0 345 225" aria-label="Sprechblase">
      <polygon points="26,62 322,16 334,154 214,172 226,214 156,180 50,196" fill="#1b1b1b"/>
      <polygon points="16,54 310,10 324,144 204,162 212,200 146,170 38,186" fill="var(--pink)"/>
      <g transform="rotate(-7 170 100)">
        <text x="40" y="96" font-size="30">ICH ARBEITE 24/7</text>
        <text x="60" y="134" font-size="30">FÜR MEINEN CHEF !</text>
      </g>
    </svg>

    <svg class="bubble bubble-green" viewBox="0 0 240 140" aria-label="Sprechblase">
      <path d="M26 12 Q22 4 34 4 L222 14 Q234 15 232 28 L226 108 Q225 120 212 120 L48 118 L18 132 L30 112 Q18 110 18 98 Z" fill="var(--green)" stroke="#1e3d16" stroke-width="2"/>
      <g transform="rotate(3 120 70)">
        <text x="42" y="56" font-size="28">UND ICH</text>
        <text x="44" y="92" font-size="28">ICH LIEBE ES !</text>
      </g>
    </svg>

    <p class="locations">Nordhafen – Weidenstadt<br>Kalmbrück/Eschau – Lindgau</p>

    <div class="url-band">
      <span class="url">stabwerkel.cloud</span>
    </div>
  </main>
</body>
</html>
```